Lumo -Fresh business card design

It is a dry cleaning carpet business.
Red wine stain removal and pet urine treatments.
Servicing all regional areas.
Updates

all logo and pictures files have been uploaded

Industry/Entity Type

Dry Cleaning

Contact Information for Business Card

Lumo-Fresh Carpet and upholstery cleaning.
Servicing Albury/Wodonga and surrounding areas.
ph gus 0461273904 ,email lumofresh1@tealpost.example

Font styles to use
Serif
Sans Serif
Other font styles liked:
• lumo fresh logo font

Colors
ec2027
ffcf3e
33a6d7
0692cd

Requirements
Nice to have
• I have included photos of the logo and car and stripe on van ,I dont need all of them in the card just i would like to stick to these colours.

```html
<!DOCTYPE html>
<html lang="en">
<head>
<meta charset="utf-8">
<title>Lumo-Fresh Business Card</title>
<link rel="stylesheet" href="https://fonts.googleapis.com/css2?family=Cabin:ital,wght@0,400;0,500;0,700;1,400&display=swap">
<style>
  :root {
    --backdrop: #8a8a8a;
    --card: #ffffff;
    --ink: #111111;
    --brand-red: #e3001b;
    --brand-blue: #0a9be2;
    --brand-yellow: #ffe800;
    --splash-text: #ffffff;
  }
  * { margin: 0; padding: 0; box-sizing: border-box; }
  html, body {
    width: 1200px;
    height: 780px;
    overflow: hidden;
    background: var(--backdrop);
    font-family: "Cabin", "Gill Sans", sans-serif;
    color: var(--ink);
  }
  .card {
    position: absolute;
    left: 54px;
    top: 60px;
    width: 1092px;
    height: 660px;
    background: var(--card);
    overflow: hidden;
  }
  .brand-name {
    position: absolute;
    top: 40px;
    left: 0;
    width: 100%;
    text-align: center;
    font-weight: 700;
    font-size: 122px;
    line-height: 1;
    letter-spacing: 2px;
    color: var(--brand-blue);
  }
  .service-line {
    position: absolute;
    top: 190px;
    left: 0;
    width: 100%;
    text-align: center;
    font-weight: 500;
    font-size: 47px;
    line-height: 1;
    letter-spacing: 0.5px;
  }
  .divider {
    position: absolute;
    top: 266px;
    left: 93px;
    width: 906px;
    height: 11px;
    background: var(--brand-red);
  }
  .service-area {
    position: absolute;
    top: 302px;
    left: 93px;
    font-style: italic;
    font-size: 40px;
    line-height: 1;
  }
  .contact {
    position: absolute;
    left: 93px;
    font-size: 38px;
    line-height: 1;
  }
  .contact--phone { top: 382px; }
  .contact--email { top: 444px; }
  .phone-number {
    color: var(--brand-red);
    font-weight: 700;
    font-size: 45px;
    letter-spacing: 1px;
  }
  .stripes {
    position: absolute;
    left: 0;
    bottom: 0;
    width: 1092px;
    height: 160px;
  }
  .splash {
    position: absolute;
    left: 706px;
    top: 378px;
    width: 320px;
    height: 220px;
  }
  .splash-shape {
    position: absolute;
    inset: 0;
    background: var(--brand-red);
    border-radius: 50%;
  }
  .splash-text {
    position: absolute;
    inset: 0;
    display: flex;
    flex-direction: column;
    align-items: center;
    justify-content: center;
    color: var(--splash-text);
    font-weight: 700;
    text-align: center;
    line-height: 1;
  }
  .splash-text .big { font-size: 60px; margin-bottom: 4px; }
  .splash-text .small { font-size: 30px; line-height: 1.1; }
</style>
</head>
<body>
  <main class="card">
    <h1 class="brand-name">LUMO-FRESH</h1>
    <p class="service-line">CARPET AND UPHOLSTERY CLEANING</p>
    <div class="divider"></div>
    <p class="service-area">Servicing Albury/Wodonga and surrounding areas</p>
    <p class="contact contact--phone">Phone Gus <span class="phone-number">0461 273 904</span></p>
    <p class="contact contact--email">Email lumofresh1@tealpost.example</p>

    <svg class="stripes" viewBox="0 0 1092 160" aria-hidden="true">
      <polygon points="0,5 1092,156 1092,160 0,160" fill="var(--brand-blue)"/>
      <polygon points="0,68 1070,160 0,160" fill="var(--brand-yellow)"/>
      <polygon points="0,87 910,160 0,160" fill="var(--brand-red)"/>
    </svg>

    <div class="splash">
      <div class="splash-shape" role="img" aria-label="Red paint splash"></div>
      <div class="splash-text">
        <span class="big">NO</span>
        <span class="small">SOGGY WET<br>CARPETS</span>
      </div>
    </div>
  </main>
</body>
</html>
```